KORVALD GmbH

We need an improvement of the existing design of our webpage (www.korvald.de).
We are a Munich based IT services company offering application consulting, system infrastructure consulting and outsourcing. We do not want to completely restructure our website, instead we want to have an improvement of the existing one. So the design should fit into the already existing page enhance or modify it and make it look more professional. For example the slideshow could be improved with pictures that better fit. Furthermore the logo could also be improved and modified. Also the tables, and layers could be improved. As a result we do not expect radical changes but rather a more clean and improved look compared to the as-is situation. The design should communicate professionalism, experience and success.

Target Market(s)

small and medium sized companies.

Requirements
Must have
• Logo improvement, slideshow improvement, table and layer improvement
Should not have
• Only care about the landing page.

```html
<!DOCTYPE html>
<html lang="de">
<head>
<meta charset="utf-8">
<title>KORVALD GmbH – IT-Dienstleistungen</title>
<link rel="stylesheet" href="https://fonts.googleapis.com/css2?family=Source+Sans+3:wght@400;600;700&family=Roboto+Condensed:wght@400;700&display=swap">
<style>
:root{
  --brand:#0d4f9e;
  --navy:#2a4070;
  --navy-dark:#233862;
  --button:#1c2d50;
  --text:#444b55;
  --heading:#27406e;
  --line:#d6d9de;
  --white:#ffffff;
  --sky-top:#9dbde0;
  --sky-bottom:#e9f1f9;
}
*{margin:0;padding:0;box-sizing:border-box}
html,body{width:1080px;height:1200px;overflow:hidden;background:var(--white)}
body{position:relative;font-family:"Source Sans 3",sans-serif;color:var(--text)}
.abs{position:absolute}

/* header */
.logo-name{left:162px;top:16px;font-size:32px;font-weight:700;color:var(--brand);letter-spacing:.3px;line-height:1}
.logo-tagline{left:163px;top:48px;font-size:14px;font-weight:600;color:var(--brand);line-height:1}
.nav a{position:absolute;top:39px;font-family:"Roboto Condensed",sans-serif;font-size:11.5px;color:#3a4f74;text-decoration:none;font-weight:400}
.nav .active{font-weight:700;color:var(--navy)}
.search{left:742px;top:34px;width:175px;height:20px;border:1px solid #d4d7dc;border-radius:3px;background:#f6f7f8;font-family:"Roboto Condensed",sans-serif;font-size:7.5px;color:#666;padding:5px 0 0 10px}
.search svg{position:absolute;right:8px;top:3px}

/* hero */
.hero{left:0;top:81px;width:1080px;height:381px;background:linear-gradient(180deg,var(--sky-top) 0%,#c5d9ee 45%,var(--sky-bottom) 100%)}
.hero-title{left:162px;top:198px;font-size:30px;font-weight:600;color:var(--brand);letter-spacing:.5px}
.hero-sub{left:162px;top:239px;font-size:18px;font-weight:600;color:#2f3640}
.hero-text{left:162px;top:265px;width:380px;font-size:12.5px;line-height:20px;color:#2f3640}
.arrow{top:240px}

/* services */
.section-title{left:0;width:1080px;text-align:center;top:490px;font-size:24px;color:var(--heading)}
.section-intro{left:190px;width:700px;text-align:center;top:530px;font-size:9.5px;line-height:18px;color:var(--text)}
.divider{left:177px;top:586px;width:730px;height:1px;background:var(--line)}
.service{top:612px;width:230px;text-align:center}
.service .badge{width:70px;height:70px;border-radius:50%;background:var(--navy);margin:0 auto;display:flex;align-items:center;justify-content:center}
.service h3{margin-top:16px;font-size:12.5px;font-weight:400;color:var(--heading)}
.service p{margin-top:10px;font-size:9px;line-height:15.5px;color:var(--text)}

/* partners */
.partners-title{left:162px;top:817px;font-size:15.5px;color:var(--heading)}
.partner{top:853px;width:185px;height:87px;border:1px solid #dcdfe3;display:flex;align-items:center;justify-content:center}
.partner span{display:block}

/* footer */
.footer{left:0;top:966px;width:1080px;height:186px;background:var(--navy)}
.footer-bar{left:0;top:1152px;width:1080px;height:48px;background:var(--navy-dark)}
.foot-h{top:988px;font-size:14.5px;color:var(--white)}
.foot-text{font-size:9px;line-height:15.6px;color:var(--white)}
.btn{background:var(--button);color:var(--white);font-size:9px;display:flex;align-items:center;justify-content:center;border-radius:2px}
.contact-item{left:494px;display:flex;gap:10px;font-size:9px;line-height:15.6px;color:var(--white)}
.contact-item svg{flex:none;margin-top:2px}
.email-input{left:674px;top:1064px;width:212px;height:22px;background:#52668c;border-radius:2px;color:var(--white);font-size:9px;padding:5px 0 0 12px}
.copyright{left:164px;top:1170px;font-size:9px;color:var(--white)}
.follow{left:794px;top:1171px;font-size:9px;color:var(--white)}
.social{top:1165px;width:23px;height:23px;border-radius:50%}
</style>
</head>
<body>

<header>
  <div class="abs logo-name">KORVALD GmbH</div>
  <div class="abs logo-tagline">IT-Dienstleistungen für Ihr Unternehmen</div>
  <nav class="nav">
    <a class="active" style="left:486px" href="#">HOME</a>
    <a style="left:568px" href="#">SERVICES</a>
    <a style="left:666px" href="#">CONTACT US</a>
  </nav>
  <div class="abs search">SEARCH :
    <svg width="14" height="14" viewBox="0 0 14 14"><circle cx="5.5" cy="5.5" r="4" fill="none" stroke="#aaa" stroke-width="1.5"/><line x1="8.5" y1="8.5" x2="12.5" y2="12.5" stroke="#aaa" stroke-width="2"/></svg>
  </div>
</header>

<section>
  <div class="abs hero" role="img" aria-label="Slideshow-Foto: Geschäftsmann im weißen Hemd mit Mobiltelefon vor blauem Himmel mit Wolken"></div>
  <div class="abs hero-title">KORVALD&nbsp; GMBH</div>
  <div class="abs hero-sub">IT-DIENSTLEISTUNGEN FUR IHR UNTERNEHME</div>
  <div class="abs hero-text">Wir sind IT-Dienstleister, spezialisiert auf die Anforderungen kleiner und mittelständischer Unternehmen (KMUs) im Raum München und Umgebung</div>
  <svg class="abs arrow" style="left:82px" width="46" height="46" viewBox="0 0 46 46"><circle cx="23" cy="23" r="21.5" fill="none" stroke="#fff" stroke-opacity=".8" stroke-width="2"/><path d="M27 13 L16 23 L27 33 Z" fill="#fff" fill-opacity=".8"/></svg>
  <svg class="abs arrow" style="left:954px" width="46" height="46" viewBox="0 0 46 46"><circle cx="23" cy="23" r="21.5" fill="none" stroke="#fff" stroke-opacity=".8" stroke-width="2"/><path d="M19 13 L30 23 L19 33 Z" fill="#fff" fill-opacity=".8"/></svg>
</section>

<section>
  <h2 class="abs section-title" style="font-weight:400">Service Portfolio</h2>
  <p class="abs section-intro">Wir sind IT-Dienstleister, spezialisiert auf die Anforderungen kleiner und mittelständischer Unternehmen (KMUs) im Raum München und Umgebung. Seit über 20 Jahren schaffen wir mit unseren drei Kernkompetenten Mehrwert für unsere Kunden:</p>
  <div class="abs divider"></div>

  <div class="abs service" style="left:162px">
    <div class="badge"><svg width="26" height="34" viewBox="0 0 26 34"><rect x="3" y="2" width="20" height="30" rx="4" fill="none" stroke="#fff" stroke-width="2.5"/><rect x="7" y="7" width="12" height="17" rx="1" fill="#fff"/><circle cx="13" cy="28" r="1.5" fill="#fff"/></svg></div>
    <h3>Applikationsbetreuung</h3>
    <p>Durch unsere langjährige Erfahrung mit diesen Produkten und zahlreichen Projekten, können wir Sie individuell beraten, setzen Lösungen effizient um und helfen Ihnen dabei einen.</p>
  </div>
  <div class="abs service" style="left:428px">
    <div class="badge"><svg width="30" height="30" viewBox="0 0 30 30"><circle cx="15" cy="15" r="6" fill="none" stroke="#fff" stroke-width="2"/><g stroke="#fff" stroke-width="2.5"><line x1="15" y1="3" x2="15" y2="7"/><line x1="15" y1="23" x2="15" y2="27"/><line x1="3" y1="15" x2="7" y2="15"/><line x1="23" y1="15" x2="27" y2="15"/><line x1="6.5" y1="6.5" x2="9.3" y2="9.3"/><line x1="20.7" y1="20.7" x2="23.5" y2="23.5"/><line x1="6.5" y1="23.5" x2="9.3" y2="20.7"/><line x1="20.7" y1="9.3" x2="23.5" y2="6.5"/></g></svg></div>
    <h3>Systembetreuung</h3>
    <p>Durch unsere langjährige Erfahrung mit diesen Produkten und zahlreichen Projekten, können wir Sie individuell beraten, setzen Lösungen effizient um und helfen Ihnen dabei einen.</p>
  </div>
  <div class="abs service" style="left:693px">
    <div class="badge"><svg width="32" height="32" viewBox="0 0 32 32"><circle cx="14" cy="18" r="11" fill="none" stroke="#fff" stroke-width="2.5"/><circle cx="14" cy="18" r="6" fill="none" stroke="#fff" stroke-width="2.5"/><circle cx="14" cy="18" r="2" fill="#fff"/><line x1="14" y1="18" x2="27" y2="5" stroke="#fff" stroke-width="2"/><path d="M24 3 L29 3 L29 8 Z" fill="#fff"/></svg></div>
    <h3>Ganzheitliche Betreuung</h3>
    <p>Durch unsere langjährige Erfahrung mit diesen Produkten und zahlreichen Projekten, können wir Sie individuell beraten, setzen Lösungen effizient um und helfen Ihnen dabei einen.</p>
  </div>
</section>

<section>
  <h2 class="abs partners-title" style="font-weight:400">Our Partners</h2>
  <div class="abs partner" style="left:162px"><span style="width:101px;height:49px;border-radius:5px;background:#5b86c4"></span></div>
  <div class="abs partner" style="left:352px"><span style="width:108px;height:49px;border-radius:2px;background:#0fa0e0"></span></div>
  <div class="abs partner" style="left:542px"><span style="width:92px;height:60px;background:#1b1b1b"></span></div>
  <div class="abs partner" style="left:731px"><span style="width:59px;height:59px;background:#6cc600"></span></div>
</section>

<footer>
  <div class="abs footer"></div>
  <h3 class="abs foot-h" style="left:162px;font-weight:400">About Korvald</h3>
  <p class="abs foot-text" style="left:162px;top:1019px;width:285px">Wir übernehmen für Sie die Administration und Optimierung ihrer IT-Infrastruktur. Durch den Einsatz von Virtualisierung können wir Ihnen helfen effizienter zu werden durch Kosteneinsparungen für den Betrieb und die Verwaltung Ihrer Systeme. Überzeugen Sie sich von unseren Erfahrungen bei namhaften Mittelständlern...</p>
  <div class="abs btn" style="left:162px;top:1105px;width:85px;height:24px">Read More</div>

  <h3 class="abs foot-h" style="left:494px;font-weight:400">Get In Touch</h3>
  <div class="abs contact-item" style="top:1022px"><svg width="13" height="17" viewBox="0 0 13 17"><path d="M6.5 0 A6.5 6.5 0 0 1 13 6.5 C13 11 6.5 17 6.5 17 C6.5 17 0 11 0 6.5 A6.5 6.5 0 0 1 6.5 0Z" fill="#fff"/><circle cx="6.5" cy="6.5" r="2.3" fill="var(--navy)"/></svg><span>Lindenweg 14,<br>82140 Olching</span></div>
  <div class="abs contact-item" style="top:1057px"><svg width="11" height="9" viewBox="0 0 11 9"><rect width="11" height="9" fill="#fff"/><path d="M0 0 L5.5 5 L11 0" fill="none" stroke="var(--navy)" stroke-width="1.2"/></svg><span>Email : info@korvald.de</span></div>
  <div class="abs contact-item" style="top:1076px"><svg width="11" height="11" viewBox="0 0 11 11"><path d="M2 0 L4 3 L3 4.5 C4 6.5 5 7.5 6.5 8 L8 7 L11 9 L9.5 11 C5 11 0 6 0 1.5Z" fill="#fff"/></svg><span>Phone : +49891234500</span></div>
  <div class="abs contact-item" style="top:1097px"><svg width="11" height="11" viewBox="0 0 11 11"><rect x="2.5" y="0" width="6" height="3" fill="#fff"/><rect x="0" y="3.5" width="11" height="5" rx="1" fill="#fff"/><rect x="2.5" y="7" width="6" height="4" fill="#fff" stroke="var(--navy)" stroke-width=".8"/></svg><span>Fax : +498912345085</span></div>

  <h3 class="abs foot-h" style="left:671px;font-weight:400">Newsletter</h3>
  <p class="abs foot-text" style="left:671px;top:1020px;width:220px">Join our mailing list to stay up to date and get notices about our new releases!</p>
  <div class="abs email-input">Enter your Email Id :</div>
  <div class="abs btn" style="left:671px;top:1102px;width:85px;height:24px">Subscribe</div>

  <div class="abs footer-bar"></div>
  <div class="abs copyright">Copyrights © 2013. Korvald. All Rights Reserved.</div>
  <div class="abs follow">Follow us :</div>
  <div class="abs social" style="left:841px;background:#3b63b5"></div>
  <div class="abs social" style="left:867px;background:#2c9ad8"></div>
  <div class="abs social" style="left:894px;background:#1d7cab"></div>
</footer>

</body>
</html>
```